Website Design for a New Business Sharing Application

Purpose: Website for a new product – a sharing application called "Gathr.io"

Product concept: Easy sharing of business information. The application has different sections: tasks, calendars, documents, contacts, notes and links. The key feature of the application is that you can drag and drop information from different sections into a "share." A share is a page which lists all the types of information that you drag into it. You can add people to this "share."

Note: The application itself is not part of this project, just the website.

Website details: The site, in addition to being informational, will actually be the first point of entry for visitors into the application itself. Because of that, we would like the website design to reflect the look of the application, to create a smooth and seamless experience for the user moving from the website into the application (tough the website does not need to look *exactly* like the application). Included Product Tour screenshots show you the look of the application.

Website pages to be created: 4 pages
We are flexible in terms of the exact structure and placement of elements. You may change that any way you like. The pages are as follows:

Home page
Product Tour page
Press page
Blog page

Specific description of pages are provided in project files we will upload. We will also upload the logo, home page layout we have in mind, and other supporting files.

NOTE: Please submit first the design of the home page. Based on this design we will ask selected designers to submit designs for the other pages.

Target Market(s)

Business people who want to share work related files with their colleagues

Industry/Entity Type

Business

Requirements
Must have
• All the required features are listed in the description of the website and specific pages that we will upload.

```html
<!DOCTYPE html>
<html lang="en">
<head>
<meta charset="utf-8">
<title>Gathr.io – Share NOW!</title>
<link rel="stylesheet" href="https://fonts.googleapis.com/css2?family=Open+Sans:wdth,wght@75..100,300..800&display=swap">
<style>
  :root {
    --header-bg: #d8d3cb;
    --stage-light: #ffffff;
    --stage-dark: #cfcfcf;
    --footer-bg: #e3e1de;
    --ink-gray: #6e6e6e;
    --ink-soft: #7c7c7c;
    --ink-faint: #b3b3b3;
    --accent-blue: #29a3dc;
    --brand-blue: #2b7cc1;
    --brand-orange: #e8731c;
    --green-top: #5fd35a;
    --green-bottom: #128a2c;
    --blue-top: #bfe7f8;
    --blue-mid: #3aa6d6;
    --blue-bottom: #0d6fa6;
    --navy-ink: #2d3e50;
    --button-orange: #f6a21b;
    --ribbon-blue: #8fd6f4;
    --white: #ffffff;
  }
  * { box-sizing: border-box; margin: 0; padding: 0; }
  html, body { width: 1200px; height: 675px; overflow: hidden; }
  body {
    position: relative;
    font-family: "Open Sans", Arial, sans-serif;
    background: var(--footer-bg);
    color: var(--ink-gray);
  }
  .site-header {
    position: absolute; left: 0; top: 0; width: 1200px; height: 85px;
    background: var(--header-bg);
  }
  .brand {
    position: absolute; left: 82px; top: 22px;
    display: flex; align-items: center; gap: 10px;
    font-size: 28px; font-weight: 700; color: var(--brand-blue);
  }
  .brand-dot {
    width: 26px; height: 26px; border-radius: 50%;
    background: var(--brand-orange);
  }
  .account-link {
    position: absolute; right: 55px; top: 26px;
    font-size: 28px; font-weight: 400; color: var(--ink-soft);
  }
  .stage {
    position: absolute; left: 0; top: 85px; width: 1200px; height: 485px;
    background: radial-gradient(ellipse 560px 360px at 600px 250px, var(--stage-light) 30%, #ececec 70%, var(--stage-dark) 100%);
  }
  .stage-shadow {
    position: absolute; left: 70px; top: 560px; width: 1060px; height: 50px;
    border-radius: 50%;
    box-shadow: 0 -14px 26px rgba(0,0,0,0.22) inset;
    clip-path: inset(10px 0 0 0);
  }
  .tagline {
    position: absolute; top: 104px; width: 1200px; text-align: center;
    font-size: 24px; font-weight: 600; color: var(--accent-blue);
  }
  .tagline .divider { margin: 0 10px; font-weight: 400; }
  .headline {
    position: absolute; top: 146px; width: 1200px; text-align: center;
    font-size: 62px; font-weight: 700; line-height: 1.1; color: var(--ink-gray);
  }
  .subheadline {
    position: absolute; top: 220px; width: 1200px; text-align: center;
    font-size: 33px; font-weight: 700; color: var(--ink-gray);
  }
  .content-types {
    position: absolute; top: 274px; width: 1200px; text-align: center;
    font-size: 25px; color: var(--ink-soft);
  }
  .content-types .sep {
    display: inline-block; margin: 0 6px; font-size: 14px; vertical-align: 3px; color: var(--ink-faint);
  }
  .drop-zone {
    position: absolute; left: 105px; top: 333px; width: 430px; height: 146px;
    border-radius: 10px; border: 2px solid #d6f2b8;
    background: linear-gradient(180deg, var(--green-top) 0%, #2eb33e 48%, var(--green-bottom) 52%, #1a9a33 100%);
    box-shadow: 0 2px 6px rgba(0,0,0,0.3);
  }
  .drop-tab {
    position: absolute; left: -2px; top: 38px; width: 97px; height: 66px;
    border-radius: 0 33px 33px 0;
    background: linear-gradient(180deg, #ffffff, #c9c9c9);
    box-shadow: 0 2px 4px rgba(0,0,0,0.3);
  }
  .drop-tab svg { position: absolute; left: 20px; top: 12px; }
  .drop-label {
    position: absolute; left: 133px; top: 10px;
    font-size: 31px; font-stretch: 85%; line-height: 40px; color: var(--white);
  }
  .or-word {
    position: absolute; left: 557px; top: 352px;
    font-size: 70px; font-weight: 400; color: var(--ink-faint);
  }
  .signup-box {
    position: absolute; left: 655px; top: 332px; width: 425px; height: 146px;
    border-radius: 10px; border: 2px solid #d6eef8;
    background: linear-gradient(180deg, var(--blue-top) 0%, #8ccfec 40%, var(--blue-mid) 55%, var(--blue-bottom) 100%);
    box-shadow: 0 2px 6px rgba(0,0,0,0.3);
  }
  .signup-title {
    position: absolute; left: 22px; top: 10px;
    font-size: 26px; font-stretch: 90%; color: var(--navy-ink);
  }
  .email-field {
    position: absolute; left: 19px; top: 56px; width: 371px; height: 33px;
    border-radius: 7px; background: var(--white);
    box-shadow: inset 0 1px 3px rgba(0,0,0,0.25);
    padding: 2px 10px; font-size: 19px; color: #8a8a8a;
  }
  .start-button {
    position: absolute; left: 147px; top: 104px; width: 114px; height: 27px;
    border-radius: 3px; border: 1px solid #8a5a0a;
    background: linear-gradient(180deg, #ffc247, var(--button-orange));
    font-size: 14px; font-weight: 600; color: var(--white); text-align: center; line-height: 25px;
  }
  .free-ribbon {
    position: absolute; left: 95px; top: 493px;
  }
  .free-ribbon span {
    position: absolute; left: 13px; top: 7px; font-size: 13px; color: #1f3a4d; white-space: nowrap;
  }
  .video-prompt {
    position: absolute; left: 443px; top: 505px; display: flex; align-items: center; gap: 14px;
    font-size: 23px; color: var(--ink-gray);
  }
  .video-button {
    display: flex; align-items: center; height: 35px; border-radius: 4px; overflow: hidden;
    background: linear-gradient(180deg, #e9e5de, #b4aea4);
    box-shadow: 0 1px 3px rgba(0,0,0,0.3);
  }
  .video-button .label { padding: 0 12px 0 10px; font-size: 21px; color: #444; }
  .video-button .play {
    width: 27px; height: 35px; background: var(--brand-orange);
    display: flex; align-items: center; justify-content: center;
  }
  .footer-nav {
    position: absolute; left: 116px; top: 623px; font-size: 13.5px; color: #555;
  }
  .footer-nav a { color: inherit; text-decoration: none; }
  .footer-nav .bar { margin: 0 6px; color: #888; }
  .social-links { position: absolute; left: 1008px; top: 615px; display: flex; gap: 12px; }
  .social-square { width: 32px; height: 32px; border-radius: 4px; }
  .social-square.one { background: #5ab5e6; }
  .social-square.two { background: #3b5a9c; }
  .social-square.three { background: #2a2a2a; }
</style>
</head>
<body>
  <header class="site-header">
    <div class="brand"><span class="brand-dot"></span>Gathr.io</div>
    <div class="account-link">Access your shares</div>
  </header>

  <main class="stage"></main>
  <div class="stage-shadow"></div>

  <p class="tagline">Certified fastest sharing in the market <span class="divider">|</span>Its social!</p>
  <h1 class="headline">Share NOW!</h1>
  <h2 class="subheadline">Drag information, add people, BOOM!</h2>
  <p class="content-types">files<span class="sep">▶</span>pictures<span class="sep">▶</span>tasks<span class="sep">▶</span>to-dos<span class="sep">▶</span>calendars<span class="sep">▶</span>notes<span class="sep">▶</span>links</p>

  <section class="drop-zone">
    <div class="drop-tab">
      <svg width="50" height="42" viewBox="0 0 50 42"><rect x="22" y="0" width="5" height="42" fill="#c77d1d"/><rect x="0" y="18" width="50" height="5" fill="#c77d1d"/></svg>
    </div>
    <div class="drop-label">DRAG FILES<br>HERE TO SHARE<br>IMMEDIATELY</div>
  </section>

  <div class="or-word">or</div>

  <section class="signup-box">
    <div class="signup-title">ENTER BUSINESS EMAIL</div>
    <div class="email-field">dmarlow@fernmail.com</div>
    <div class="start-button">Start Sharing</div>
  </section>

  <div class="free-ribbon">
    <svg width="182" height="64" viewBox="0 0 182 64">
      <polygon points="0,0 182,0 172,29 0,29" fill="var(--ribbon-blue)"/>
      <polygon points="80,29 100,29 90,62" fill="#1d8fc4"/>
    </svg>
    <span>FREE! For unlimited users</span>
  </div>

  <div class="video-prompt">
    <span>What is it?</span>
    <div class="video-button">
      <span class="label">Watch Video</span>
      <span class="play"><svg width="12" height="16" viewBox="0 0 12 16"><polygon points="0,0 12,8 0,16" fill="#fff"/></svg></span>
    </div>
  </div>

  <nav class="footer-nav">
    <a href="#">Home</a><span class="bar">|</span><a href="#">About Us</a><span class="bar">|</span><a href="#">Product Tour</a><span class="bar">|</span><a href="#">Pricing</a><span class="bar">|</span><a href="#">Terms Of Use</a><span class="bar">|</span><a href="#">Jobs</a><span class="bar">|</span><a href="#">Sign Up</a><span class="bar">|</span><a href="#">Blog</a><span class="bar">|</span><a href="#">Press</a><span class="bar">|</span><a href="#">Contact Us</a>
  </nav>

  <div class="social-links">
    <span class="social-square one" role="img" aria-label="Social network link"></span>
    <span class="social-square two" role="img" aria-label="Social network link"></span>
    <span class="social-square three" role="img" aria-label="Social network link"></span>
  </div>
</body>
</html>
```